brevity cafe flyer design project

A funky trendy cafe in Melbourne’s CBD that caters too a large range of corporate clients. Located on the door step of a major train station, its a quick turn around cafe for the short time frame customer but also a cafe to sit, relax and enjoy the hustle and bustle from the inside out. We provide All day breakfast, gourmet sandwiches, gourmet rotti wraps, a la carte menu and also heat and serve meals.

BREAKFAST TO GO! ALL BREAKFAST TO GO ITEMS COME WITH A MEDIUM TAKE AWAY COFFEE!
• RAISIN TOAST & COFFEE – $6
• BACON & EGG MUFFIN & COFFEE $7.5
• SPINACH, MUSHROOM OMELETTE MUFFIN & COFFEE $7.5
• OMELETTE WITH CHEESE MUFFIN & COFFEE $7.5
• HAM & CHEESE CROISSANT & COFFEE $7.5
• SWEET OR SAVOURY MUFFIN & COFFEE $6.5
• HAM & CHEESE SANDWICH & COFFEE $8.0
• HAM, CHEESE & TOMATO SANDWICH & COFFEE $8.5

*NOT IN CONJUNCTION WITH BREVITY CLUB CARD OFFER

WE ALSO HAVE PRE-MADE LUNCH OPTIONS – ASSORTED ROTTI WRAPS (Bbq chicken, honey mustard chicken, pesto chicken & vegetarian) ASSORTED GOURMET SANDWICHES (Mediterranean, Moroccan chicken, Salami, Chicken Schnitzel, Salmon, Brevity & Roast Beef) Soup of the day Pasta of the day Salad of the day

Ph- 03 9718 4630 Fax- 03 9718 4637 Web – www.brevitycafe.com.au 182 DORNAL STREET MELBOURNE 3000

Industry/Entity Type

Cafe

Font styles to use
Serif

Requirements
Must have
• Our 2 branded colours -

PMS 392c
PMS BLACK

```html
<!DOCTYPE html>
<html lang="en">
<head>
<meta charset="utf-8">
<title>Brevity Cafe – Breakfast To Go</title>
<link rel="stylesheet" href="https://fonts.googleapis.com/css2?family=Open+Sans:wght@300;400;600;700&display=swap">
<style>
  :root {
    --lime: #a6d11e;
    --black: #111111;
    --ink: #1a1a1a;
    --grey-text: #5a5a5a;
    --leader: #9a9a9a;
    --paper: #ffffff;
    --swirl-a: #f3f3f3;
    --swirl-b: #dcdcdc;
    --coffee-dark: #3b2516;
    --coffee-mid: #8a5a32;
    --coffee-light: #d8b48a;
  }
  * { margin: 0; padding: 0; box-sizing: border-box; }
  html, body { width: 1200px; height: 2544px; overflow: hidden; }
  body {
    position: relative;
    font-family: "Open Sans", Arial, sans-serif;
    color: var(--ink);
    background: var(--paper);
  }
  .backdrop-pattern {
    position: absolute; inset: 0;
    background:
      radial-gradient(ellipse at 20% 30%, var(--swirl-b) 0%, transparent 40%),
      radial-gradient(ellipse at 85% 60%, var(--swirl-b) 0%, transparent 38%),
      radial-gradient(ellipse at 30% 85%, var(--swirl-b) 0%, transparent 35%),
      var(--swirl-a);
  }
  .photo-grid {
    position: absolute; left: 55px; top: 64px; width: 1090px; height: 1219px;
    background: var(--paper);
  }
  .photo {
    position: absolute;
    background: radial-gradient(circle at 50% 45%, var(--coffee-light) 0%, var(--coffee-mid) 35%, var(--coffee-dark) 80%);
  }
  .logo-cell {
    position: absolute; left: 341px; top: 406px; width: 401px; height: 399px;
    background: var(--paper);
  }
  .logo-square {
    position: absolute; left: 35px; top: 35px; width: 340px; height: 335px;
    background: var(--black);
    display: flex; align-items: center; justify-content: center;
  }
  .logo-name {
    color: var(--lime); font-weight: 400; font-size: 40px; letter-spacing: 2px;
    text-transform: uppercase;
  }
  .menu { position: absolute; left: 161px; top: 1380px; width: 880px; }
  .menu-item {
    position: absolute; left: 0; width: 880px;
    display: flex; align-items: flex-start;
    font-size: 37px; line-height: 50px; letter-spacing: -0.5px;
  }
  .item-name { width: 710px; display: flex; white-space: nowrap; }
  .item-name .lead {
    flex: 1; border-bottom: 3px dotted var(--leader);
    margin: 0 4px 13px; height: 36px;
  }
  .item-name.wrap { display: block; }
  .item-name.wrap .line-full {
    display: block; text-align: justify; text-align-last: justify; letter-spacing: 2px;
  }
  .item-name.wrap .line-end { display: block; }
  .price { position: absolute; left: 761px; font-weight: 700; font-size: 38px; }
  .lunch { position: absolute; left: 161px; top: 2075px; width: 878px; }
  .lunch-title { font-weight: 700; font-size: 27px; color: var(--grey-text); }
  .lunch-copy { font-size: 19.5px; line-height: 26px; color: var(--grey-text); text-align: justify; }
  .contact-bar {
    position: absolute; left: 55px; top: 2260px; width: 1090px; height: 150px;
    background: var(--black); text-align: center; color: var(--lime);
  }
  .contact-phone { font-weight: 600; font-size: 38px; padding-top: 16px; line-height: 52px; }
  .contact-address { font-weight: 300; font-size: 51px; line-height: 62px; letter-spacing: 0.5px; }
  .web-bar {
    position: absolute; left: 55px; top: 2415px; width: 1090px; height: 56px;
    background: var(--lime); text-align: center;
    font-weight: 700; font-size: 40px; line-height: 56px; letter-spacing: 8px; color: var(--black);
  }
</style>
</head>
<body>
  <div class="backdrop-pattern" role="img" aria-label="Soft grey decorative swirl pattern"></div>

  <section class="photo-grid">
    <div class="photo" style="left:0;top:0;width:333px;height:398px" role="img" aria-label="Cappuccino with heart latte art on red saucer"></div>
    <div class="photo" style="left:341px;top:0;width:401px;height:398px" role="img" aria-label="Large mug of latte with fern latte art"></div>
    <div class="photo" style="left:750px;top:0;width:340px;height:398px" role="img" aria-label="Two coffees and a bowl of brown sugar on a table"></div>
    <div class="photo" style="left:0;top:406px;width:333px;height:399px" role="img" aria-label="Latte with heart art beside a notebook"></div>
    <div class="logo-cell">
      <div class="logo-square"><span class="logo-name">brevity cafe</span></div>
    </div>
    <div class="photo" style="left:750px;top:406px;width:340px;height:399px" role="img" aria-label="Coffee cup next to a red planner and pen"></div>
    <div class="photo" style="left:0;top:813px;width:333px;height:406px" role="img" aria-label="Coffee beside an e-reader"></div>
    <div class="photo" style="left:341px;top:813px;width:401px;height:406px" role="img" aria-label="Flat white with rosetta art and paper bag"></div>
    <div class="photo" style="left:750px;top:813px;width:340px;height:406px" role="img" aria-label="Close-up of fern latte art"></div>
  </section>

  <section class="menu">
    <div class="menu-item" style="top:0"><span class="item-name">RAISIN TOAST &amp; COFFEE<span class="lead"></span></span><span class="price">$6</span></div>
    <div class="menu-item" style="top:66px"><span class="item-name">BACON &amp; EGG MUFFIN &amp; COFFEE<span class="lead"></span></span><span class="price">$7.5</span></div>
    <div class="menu-item" style="top:132px"><span class="item-name wrap"><span class="line-full">SPINACH, MUSHROOM OMELETTE</span><span class="line-end">MUFFIN &amp; COFFEE</span></span><span class="price">$7.5</span></div>
    <div class="menu-item" style="top:252px"><span class="item-name wrap"><span class="line-full">OMELETTE WITH CHEESE MUFFIN &amp;</span><span class="line-end">COFFEE</span></span><span class="price">$7.5</span></div>
    <div class="menu-item" style="top:372px"><span class="item-name">HAM &amp; CHEESE CROISSANT &amp; COFFEE<span class="lead"></span></span><span class="price">$7.5</span></div>
    <div class="menu-item" style="top:440px"><span class="item-name">SWEET OR SAVOURY MUFFIN &amp; COFFEE<span class="lead"></span></span><span class="price">$6.5</span></div>
    <div class="menu-item" style="top:508px"><span class="item-name">HAM &amp; CHEESE SANDWICH &amp; COFFEE<span class="lead"></span></span><span class="price">$8.0</span></div>
    <div class="menu-item" style="top:576px"><span class="item-name wrap"><span class="line-full">HAM, CHEESE &amp; TOMATO SANDWICH</span><span class="line-end">&amp; COFFEE</span></span><span class="price">$8.5</span></div>
  </section>

  <section class="lunch">
    <h2 class="lunch-title">PRE-MADE LUNCH OPTIONS</h2>
    <p class="lunch-copy">ASSORTED ROTTI WRAPS (Bbq chicken, honey mustard chicken, pesto chicken &amp; vegetarian) ASSORTED GOURMET SANDWICHES (Mediterranean, Moroccan chicken, Salami, Chicken Schnitzel, Salmon, Brevity &amp; Roast Beef) Soup of the day Pasta of the day Salad of the day.</p>
  </section>

  <footer>
    <div class="contact-bar">
      <p class="contact-phone">Ph: 03 9718 4630 Fax: 03 9718 4637</p>
      <p class="contact-address">182 DORNAL STREET MELBOURNE 3000</p>
    </div>
    <div class="web-bar">www.brevitycafe.com.au</div>
  </footer>
</body>
</html>
```